TRV Mechanical Solutions Business Card Design

Business card design

Thinking just large logo on one side with a phone number and the back side is contact info with services we offer with a industrial plant across the bottom of the card

See must haves. I will be laser etching these business cards on black metal business cards as well as full color card stock. So must be bold and professional.

Target Market(s)

Industrial manufacturing

Contact Information for Business Card

Industrial manufacturing construction business specializing in consulting project managment and completing projects turn key

Font styles to use
Other font styles liked:
• See Logo for colors and font style

Requirements
Must have
• TRV Mechanical Solutions
• Gerald Munroe
• 2847 Alderwick Lane
• Bel Air, MD, 21047
• Project Managment
• Consulting
• Turn Key Industrial Projects
• I’d like a industrial manufacturing “cityline” on the back side bottom of the
• I’d like to be able to print these business cards in regular color on card stock but I’d also like the design to be etched into black metal business cards

```html
<!DOCTYPE html>
<html lang="en">
<head>
<meta charset="utf-8">
<title>TRV Mechanical Solutions – Business Card</title>
<link href="https://fonts.googleapis.com/css2?family=Work+Sans:wght@400;500;600&display=swap" rel="stylesheet">
<style>
  :root {
    --stage: #8a8a8a;
    --card: #1c1c1d;
    --silver: #c9c9c9;
    --silver-dim: #8e8e8e;
    --silver-bright: #ececec;
    --rule: #6f6f6f;
  }
  * { margin: 0; padding: 0; box-sizing: border-box; }
  html, body { width: 1200px; height: 900px; overflow: hidden; }
  body {
    background: var(--stage);
    font-family: "Work Sans", sans-serif;
    color: var(--silver);
    position: relative;
  }
  .card {
    position: absolute;
    left: 250px;
    width: 700px;
    height: 400px;
    background: var(--card);
    border-radius: 4px;
    overflow: hidden;
  }
  .card--back { top: 35px; }
  .card--front { top: 465px; }

  /* shared wordmark */
  .wordmark {
    display: flex;
    align-items: center;
    gap: 12px;
    color: var(--silver);
    font-weight: 600;
    text-transform: uppercase;
    letter-spacing: 0.04em;
    white-space: nowrap;
  }
  .wordmark__square {
    background: var(--silver);
    flex: none;
  }

  /* back */
  .card--back .wordmark {
    position: absolute; left: 48px; top: 60px;
    width: 320px; font-size: 17px;
  }
  .card--back .wordmark__square { width: 14px; height: 14px; }
  .person { position: absolute; right: 48px; top: 52px; width: 240px; text-align: right; }
  .person__name { font-size: 24px; font-weight: 500; letter-spacing: 0.03em; color: var(--silver-bright); white-space: nowrap; }
  .person__role { font-size: 12px; color: var(--silver-dim); margin-top: 2px; }
  .rule { position: absolute; height: 1px; background: var(--rule); }
  .rule--top { left: 48px; right: 48px; top: 128px; }
  .rule--bottom { left: 48px; width: 320px; top: 272px; }
  .services { position: absolute; right: 48px; top: 150px; list-style: none; text-align: right; }
  .services li {
    font-size: 15px; line-height: 30px; color: var(--silver);
    display: flex; justify-content: flex-end; align-items: center; gap: 10px;
  }
  .services li::after { content: ""; width: 8px; height: 8px; background: var(--silver-dim); }
  .contact { position: absolute; left: 48px; top: 292px; list-style: none; }
  .contact li { font-size: 15px; line-height: 28px; display: flex; align-items: center; gap: 12px; }
  .contact svg { width: 14px; height: 14px; fill: none; stroke: var(--silver); stroke-width: 1.6; }

  /* front */
  .card--front .wordmark {
    position: absolute; left: 0; right: 0; top: 100px;
    justify-content: center; font-size: 34px;
  }
  .card--front .wordmark__square { width: 24px; height: 24px; }
  .address {
    position: absolute; left: 0; right: 0; top: 190px;
    text-align: center; font-size: 17px; letter-spacing: 0.03em; color: var(--silver-bright);
  }
  .skyline {
    position: absolute; left: 0; right: 0; bottom: 0; height: 150px;
    background: linear-gradient(100deg, #9c9c9c 0%, #d8d8d8 30%, #f2f2f2 45%, #8d8d8d 65%, #c4c4c4 100%);
  }
</style>
</head>
<body>

  <section class="card card--back" aria-label="Card back">
    <div class="wordmark"><span class="wordmark__square"></span>TRV Mechanical Solutions</div>
    <div class="person">
      <div class="person__name">GERALD MUNROE</div>
      <div class="person__role">Director</div>
    </div>
    <div class="rule rule--top"></div>
    <ul class="services">
      <li>Project Managment</li>
      <li>Consulting</li>
      <li>Turn Key Industrial Projects</li>
    </ul>
    <div class="rule rule--bottom"></div>
    <ul class="contact">
      <li><svg viewBox="0 0 16 16"><path d="M3 2h3l1.5 3.5-2 1.2a8 8 0 0 0 3.8 3.8l1.2-2L14 10v3a1 1 0 0 1-1 1A11 11 0 0 1 2 3a1 1 0 0 1 1-1z"/></svg>330 555-0142</li>
      <li><svg viewBox="0 0 16 16"><rect x="1.5" y="3.5" width="13" height="9"/><path d="M1.5 3.5 8 9l6.5-5.5"/></svg>info@trvmechanical.com</li>
      <li><svg viewBox="0 0 16 16"><circle cx="8" cy="8" r="6.5"/><path d="M1.5 8h13M8 1.5c-3 3.5-3 9.5 0 13M8 1.5c3 3.5 3 9.5 0 13"/></svg>www.trvmechanical.com</li>
    </ul>
  </section>

  <section class="card card--front" aria-label="Card front">
    <div class="wordmark"><span class="wordmark__square"></span>TRV Mechanical Solutions</div>
    <p class="address">2847 Alderwick Lane Bel Air, MD, 21047</p>
    <div class="skyline" role="img" aria-label="Silver industrial city skyline with plant buildings and cranes along the bottom edge"></div>
  </section>

</body>
</html>
```